Social Media Graphics - Copperfield Loop

Create 6-7 individual social media graphics (square size) to encourage folks to join our online course, using either of the text below (only one set of text per graphic:

The Lantern Ridge Method
How to Create a 7-Figure Business From Scratch
Sign Up Today!

Or

The Lantern Ridge Method
Fast-track Your Way to a Multi-Million Business!
Sign Up Today!

For the color scheme of the graphics, use 1 or 2 colors in the color palette attached; or use any colors that look nice with their outfits; AVOID using red, white and blue altogether because it will look like an Independence Day (4th of July) graphic and we don’t want that; make sure the graphics appeal to both men and women

Make sure each graphic contains 1 of the 2 pics attached; and make sure one of the graphics is all TEXT only.

Target Market(s)

men and women looking to make more money

Industry/Entity Type

entrepreneurship

Requirements
Must have
• see the text document attached
Nice to have
• We are open to a nice color design; the color palette colors are not required, especially we don't want red, white and blue used together
Should not have
• AVOID using red, white and blue altogether because it will look like an Independence Day (4th of July) graphic and we dont want that

```html
<!DOCTYPE html>
<html lang="en">
<head>
<meta charset="utf-8">
<title>Copperfield Loop – The Lantern Ridge Method social set</title>
<link href="https://fonts.googleapis.com/css2?family=Inter:wght@400;600;700;800;900&display=swap" rel="stylesheet">
<style>
:root{
  --red:#e8283c;
  --blue:#3030cc;
  --ink:#0d0d0d;
  --paper:#ffffff;
  --grey:#ededed;
  --blush:#f7c9cd;
  --denim:#2b4f86;
  --knit:#1c1e24;
}
*{box-sizing:border-box;margin:0;padding:0}
html,body{width:1200px;height:804px;overflow:hidden;background:var(--paper);font-family:"Inter",sans-serif;color:var(--ink)}
.canvas{position:relative;width:1200px;height:804px}
.tile{position:absolute;width:376px;height:376px;overflow:hidden;background:var(--grey)}
.t1{left:15px;top:17px}.t2{left:412px;top:17px}.t3{left:809px;top:17px}
.t4{left:15px;top:415px}.t5{left:412px;top:415px}.t6{left:809px;top:415px}
.abs{position:absolute}
.title{font-weight:900;line-height:.95;letter-spacing:-.5px}
.title .accent-red{color:var(--red)}
.title .accent-blue{color:var(--blue)}
.caps{text-transform:uppercase;letter-spacing:-1px}
.sub{font-weight:400;font-size:15px;line-height:1.2}
.sub b{font-weight:700}
.btn{position:absolute;height:25px;border-radius:4px;color:var(--paper);font-size:11.5px;font-weight:600;display:flex;align-items:center;justify-content:center}
.btn.red{background:var(--red)}.btn.blue{background:var(--blue)}
.center{text-align:center;left:0;right:0}
.photo{position:absolute}
/* tile 1 */
.t1{background:linear-gradient(180deg,var(--grey) 55%,#f3b4bb 100%)}
.t1 .photo{left:147px;top:101px;width:229px;height:275px;background:linear-gradient(90deg,#d62c4a 0%,#c93050 50%,#2a2628 55%,#1a1a1c 100%);border-radius:90px 90px 0 0}
/* tile 2 */
.t2{background:
  radial-gradient(circle at 100% 10%,rgba(232,60,80,.75),rgba(232,60,80,0) 30%),
  radial-gradient(circle at 10% 95%,rgba(232,60,80,.7),rgba(232,60,80,0) 30%),
  #f3f3f3}
/* tile 3 */
.t3{background:linear-gradient(180deg,var(--grey) 55%,#f0a7b0 100%)}
.t3 .frame{left:16px;top:19px;width:345px;height:195px;border-radius:18px;background:linear-gradient(180deg,#fbd3d6 0%,#f19aa3 100%);overflow:hidden}
.t3 .frame .photo{left:70px;top:6px;width:210px;height:189px;border-radius:80px 80px 0 0;background:linear-gradient(90deg,var(--knit) 50%,var(--denim) 50%)}
/* tile 4 */
.t4 .photo{left:0;top:105px;width:300px;height:271px;border-radius:110px 110px 0 0;background:linear-gradient(90deg,var(--knit) 0%,#22242b 48%,var(--denim) 52%,#1f3d6d 100%)}
.t4 .card{left:233px;top:194px;width:143px;height:93px;background:rgba(245,245,245,.94);border-radius:10px 0 0 10px;padding:13px 0 0 15px;font-weight:800;font-size:14px;line-height:1.12;white-space:nowrap}
.t4 .card span{color:var(--blue)}
/* tile 5 */
.t5{background:var(--blue)}
.t5 .card{left:38px;top:65px;width:300px;height:243px;border-radius:12px;background:var(--paper)}
/* tile 6 */
.t6 .photo{left:34px;top:90px;width:310px;height:286px;border-radius:120px 120px 0 0;background:linear-gradient(90deg,var(--knit) 0%,#22242b 50%,var(--denim) 54%,#1f3d6d 100%)}
.t6 .glass{left:92px;top:255px;width:201px;height:65px;border-radius:10px;background:rgba(205,210,222,.82);text-align:center;padding-top:7px;font-size:14px;line-height:1.15}
.t6 .glass b{color:var(--blue);font-weight:700}
</style>
</head>
<body>
<div class="canvas">

  <section class="tile t1">
    <div class="photo" role="img" aria-label="Photo of the two course hosts, arms crossed and smiling"></div>
    <h2 class="abs title" style="left:21px;top:28px;font-size:29px">The <span class="accent-red">Lantern Ridge</span><br>Method</h2>
    <p class="abs sub" style="left:21px;top:111px">How to Create a<br><b>7-Figure Business</b><br>From Scratch</p>
    <div class="btn red" style="left:21px;top:179px;width:120px">Sign Up Today!</div>
  </section>

  <section class="tile t2">
    <h2 class="abs title center" style="top:125px;font-size:33px">The <span class="accent-red">Lantern Ridge</span><br>Method</h2>
    <p class="abs sub center" style="top:210px;font-size:16px">How to Create a 7-Figure<br>Business From Scratch</p>
    <div class="btn red" style="left:128px;top:271px;width:120px">Sign Up Today!</div>
  </section>

  <section class="tile t3">
    <div class="abs frame"><div class="photo" role="img" aria-label="Photo of the two course hosts in black knit and denim"></div></div>
    <h2 class="abs title center" style="top:225px;font-size:28px">The <span class="accent-red">Lantern Ridge</span><br>Method</h2>
    <p class="abs sub center" style="top:292px;font-size:13.5px;line-height:1.15">How to Create a 7-Figure Business<br>From Scratch</p>
    <div class="btn red" style="left:131px;top:332px;width:120px">Sign Up Today!</div>
  </section>

  <section class="tile t4">
    <div class="photo" role="img" aria-label="Photo of the two course hosts smiling, arms crossed"></div>
    <h2 class="abs title caps" style="left:30px;top:32px;font-size:34px">The <span class="accent-blue">Lantern</span><br><span class="accent-blue">Ridge</span> Method</h2>
    <div class="abs card"><span>Fast-track Your</span><br><span>Way</span> to a<br>Multi-Million<br>Business!</div>
    <div class="btn blue" style="left:262px;top:293px;width:87px;font-size:9px">Sign Up Today!</div>
  </section>

  <section class="tile t5">
    <div class="abs card"></div>
    <h2 class="abs title caps center" style="top:112px;font-size:29px">The <span class="accent-blue">Lantern Ridge</span><br>Method</h2>
    <p class="abs sub center" style="top:190px;font-size:15.5px">How to Create a 7-Figure Business<br>From Scratch</p>
    <div class="btn blue" style="left:128px;top:238px;width:120px">Sign Up Today!</div>
  </section>

  <section class="tile t6">
    <div class="photo" role="img" aria-label="Photo of the two course hosts, arms crossed"></div>
    <h2 class="abs title caps center" style="top:24px;font-size:30px">The <span class="accent-blue">Lantern Ridge</span><br>Method</h2>
    <div class="abs glass">How to Create a<br><b>7-Figure Business</b> From<br>Scratch</div>
    <div class="btn blue" style="left:134px;top:328px;width:120px">Sign Up Today!</div>
  </section>

</div>
</body>
</html>
```